Verdell Chiropractic, achieve your health goals, get better each day one step at a time

A mobile friendly site, fresh look, easy to navigate, has interface with pw/chirply, etc. Blog posts. Uses new logo. Content and address to current site is mirvaton.com. The current site will give you scope of project for content. The logo is not the final but close. Will upload final next week.
Convey the concept that heath is a process, it does not just happen. We take steps to achieve what we want in life including health.

Target Market(s)

30 to 70 year old. Needing health care

Industry/Entity Type

Health Care

Coding

Coded - Design and coding required

Number of Pages Required

5+ page

Font styles to use
Sans Serif

Colors

Designer to choose colors to be used in the design.

Requirements
Must have
• mobile friendly, easy to navigate, PW/Chirply interface, blog, room for current content
Nice to have
• potential for commerce, statistics
Should not have
• Same old look and feel as everything else out there

```html
<!DOCTYPE html>
<html lang="en">
<head>
<meta charset="utf-8">
<title>Verdell Chiropractic</title>
<link rel="stylesheet" href="https://fonts.googleapis.com/css2?family=Poppins:ital,wght@0,300;0,400;0,500;0,600;0,700;1,300;1,400&display=swap">
<style>
:root{
  --blue:#4a8ec6;
  --blue-deep:#2f79b6;
  --green:#8dc63f;
  --ink:#3d3d3d;
  --muted:#6b6b6b;
  --pale:#f4f8fc;
  --footer:#2b2b2b;
  --white:#ffffff;
}
*{box-sizing:border-box;margin:0;padding:0}
html,body{width:1200px;height:2786px;overflow:hidden}
body{position:relative;font-family:"Poppins",sans-serif;color:var(--ink);background:var(--white)}
.abs{position:absolute}

/* header */
.topbar{left:0;top:0;width:1200px;height:70px;background:var(--pale)}
.brand{left:87px;top:18px;font-size:25px;font-weight:700;color:var(--blue-deep);letter-spacing:.5px;line-height:34px}
.contact-chip{top:18px;display:flex;align-items:center;gap:12px;font-size:17px;color:var(--ink);height:34px}
.contact-chip svg{width:30px;height:30px}
.nav{left:0;top:70px;width:1200px;height:32px;background:rgba(60,60,60,.82);display:flex;justify-content:center;gap:40px;padding-left:90px;z-index:2}
.nav a{color:#fff;text-decoration:none;font-size:17px;line-height:32px}

/* hero */
.hero{left:0;top:70px;width:1200px;height:460px;background:linear-gradient(100deg,#d9dfe3 0%,#eef1f3 35%,#c9d3da 60%,#9fb1c0 80%,#e6ebee 100%)}
.hero-card{left:87px;top:212px;width:413px;height:132px;background:rgba(74,142,198,.95);text-align:center;padding-top:14px}
.hero-card h1{color:#fff;font-size:42px;font-weight:700;line-height:50px;letter-spacing:1px}
.hero-card p{color:#e9f2fa;font-size:14px;line-height:26px;padding:0 20px}
.hero-btn{left:87px;top:344px;width:413px;height:46px;background:var(--green);color:#fff;font-size:13px;letter-spacing:4px;text-align:center;line-height:46px;font-weight:500}

/* about */
.about{left:0;top:530px;width:1200px;height:250px;background:var(--pale)}
.eyebrow{font-size:12px;color:var(--green);text-transform:uppercase;letter-spacing:.5px}
.about .eyebrow{left:87px;top:100px}
.about h2{left:87px;top:113px;font-size:31px;font-weight:700;color:var(--blue-deep);letter-spacing:.5px}
.about .divider{left:339px;top:83px;width:1px;height:90px;background:#cfd6dd}
.about p{left:438px;top:72px;width:660px;font-size:14.5px;line-height:27px;color:#4a4a4a}
.about p a{color:#222;text-decoration:underline;font-weight:500;font-size:13px}

/* services */
.services{left:0;top:780px;width:1200px;height:507px;background:linear-gradient(90deg,rgba(74,142,198,.96),rgba(74,142,198,.9) 60%,rgba(90,150,200,.88))}
.services .eyebrow{left:0;width:1200px;top:72px;text-align:center}
.services h2{left:0;width:1200px;top:86px;text-align:center;color:#fff;font-size:31px;font-weight:700;letter-spacing:.5px}
.hub{left:505px;top:167px;width:190px;height:190px;border-radius:50%;background:#fff;display:flex;align-items:center;justify-content:center;text-align:center;font-size:17px;font-weight:700;color:var(--blue-deep);line-height:22px;box-shadow:0 6px 18px rgba(0,0,0,.18)}
.spoke{height:1px;background:rgba(255,255,255,.45)}
.svc-dot{width:56px;height:56px;border-radius:50%;background:var(--green);display:flex;align-items:center;justify-content:center}
.svc-dot span{width:22px;height:22px;border-radius:50%;border:3px solid #fff}
.svc-label{color:#fff;font-size:17px;font-weight:500;letter-spacing:.5px;line-height:20px}
.svc-label.l{text-align:right;width:240px}
.more-link{left:0;width:1200px;top:411px;text-align:center;color:#fff;font-size:13px;text-decoration:underline;letter-spacing:.5px}

/* faq */
.faq{left:0;top:1287px;width:1200px;height:585px;background:linear-gradient(90deg,#e7e9ea 0%,#d8dcdf 25%,#c9cfd4 45%,#eaeaea 62%,#ececec 100%)}
.faq .eyebrow{left:702px;top:93px}
.faq h2{left:702px;top:106px;font-size:31px;font-weight:700;color:var(--blue-deep);letter-spacing:.5px}
.faq-item{left:702px;width:413px;height:43px;background:#fff;display:flex;align-items:center;justify-content:space-between;padding:0 18px;font-size:16px;color:#333}
.faq-item.open{background:var(--green);color:#fff}
.faq-item svg{width:12px;height:12px}
.faq-answer{left:712px;top:218px;width:395px;font-size:14px;line-height:27px;color:#444}

/* testimonials */
.testimonials{left:0;top:1872px;width:1200px;height:565px;background:linear-gradient(180deg,#f1f5f8 0%,#e8eef2 55%,#dfe6eb 100%)}
.testimonials .eyebrow{left:0;width:1200px;top:86px;text-align:center}
.testimonials h2{left:0;width:1200px;top:99px;text-align:center;font-size:31px;font-weight:700;color:var(--blue-deep);letter-spacing:.5px}
.quote-card{top:186px;width:463px;height:273px;border:2px solid #b6d88a;padding:40px 26px 0 28px}
.quote-card p{font-size:14.5px;font-style:italic;font-weight:300;line-height:26.5px;color:#555}
.quote-card cite{display:block;margin-top:10px;font-style:normal;font-weight:600;font-size:14px;color:var(--blue)}
.qmark{width:38px;height:38px;border-radius:50%;background:#fff;border:2px solid var(--green);display:flex;align-items:center;justify-content:center;color:var(--green);font-size:34px;font-weight:700;line-height:1;padding-top:12px}
.arrow{width:16px;height:16px}

/* cta */
.cta{left:0;top:2437px;width:1200px;height:82px;background:var(--blue)}
.cta p{left:175px;top:0;line-height:82px;color:#fff;font-size:17px}
.cta .btn{left:702px;top:19px;width:323px;height:44px;background:var(--green);color:#fff;font-size:13px;letter-spacing:4px;text-align:center;line-height:44px;font-weight:500}

/* footer */
.footer{left:0;top:2519px;width:1200px;height:267px;background:var(--footer);color:#cfcfcf}
.footer .brand{left:87px;top:52px;font-size:22px;color:var(--blue)}
.footer .blurb{left:87px;top:104px;width:250px;font-size:12px;line-height:21px;color:#cfcfcf}
.footer .copy{left:87px;top:214px;font-size:11.5px;color:#cfcfcf}
.footer h4{font-size:12.5px;font-weight:600;color:var(--blue);letter-spacing:.5px;top:72px}
.footer ul{list-style:none;top:105px;font-size:12px;line-height:21px}
.footer ul li::before{content:"›";color:var(--green);margin-right:9px}
.footer .info{top:105px;font-size:12px;line-height:21px}
.info-row{display:flex;gap:12px;margin-bottom:8px}
.info-row svg{width:12px;height:12px;margin-top:4px;flex:none}
</style>
</head>
<body>

<!-- header -->
<div class="abs topbar"></div>
<div class="abs brand">Verdell Chiropractic</div>
<div class="abs contact-chip" style="left:713px">
  <svg viewBox="0 0 30 30"><circle cx="15" cy="15" r="13" fill="none" stroke="#2f79b6" stroke-width="2"/><path d="M10.5 8.5l3 3-1.6 2a9 9 0 0 0 4.6 4.6l2-1.6 3 3-2 2c-6 0-11-5-11-11z" fill="#2f79b6"/></svg>
  555.210.4400
</div>
<div class="abs contact-chip" style="left:915px">
  <svg viewBox="0 0 30 30"><circle cx="15" cy="15" r="13" fill="none" stroke="#2f79b6" stroke-width="2"/><rect x="8.5" y="10" width="13" height="10" rx="1" fill="#2f79b6"/><path d="M9 11l6 5 6-5" fill="none" stroke="#fff" stroke-width="1.4"/></svg>
  info@mirvaton.com
</div>

<section class="abs hero" role="img" aria-label="Photo of a chiropractor explaining a spine model to a patient"></section>
<nav class="abs nav">
  <a href="#">Home</a><a href="#">Meet Dr. Marlow</a><a href="#">Testimonials</a><a href="#">FAQs</a><a href="#">Resources</a><a href="#">Contact</a>
</nav>
<div class="abs hero-card">
  <h1>LOREM IPSUM</h1>
  <p>It is a long established fact that a reader will be distracted by the readable content of a page.</p>
</div>
<div class="abs hero-btn">MAKE AN APPOINTMENT</div>

<!-- about -->
<section class="abs about">
  <div class="abs eyebrow">Who we are</div>
  <h2 class="abs">ABOUT US</h2>
  <div class="abs divider"></div>
  <p class="abs">The point of using Lorem Ipsum is that it has a more-or-less normal distribution of letters, as opposed to using 'Content here, content here', making it look like readable English. Many desktop publishing packages and web page editors now use Lorem Ipsum as their default model text, and a search for 'lorem ipsum' will uncover many web sites... <a href="#">READ MORE</a></p>
</section>

<!-- services -->
<section class="abs services" aria-label="Our services">
  <div class="abs eyebrow">What we do</div>
  <h2 class="abs">OUR SERVICES</h2>

  <div class="abs spoke" style="left:386px;top:180px;width:114px"></div>
  <div class="abs spoke" style="left:386px;top:258px;width:114px"></div>
  <div class="abs spoke" style="left:386px;top:336px;width:114px"></div>
  <div class="abs spoke" style="left:700px;top:180px;width:114px"></div>
  <div class="abs spoke" style="left:700px;top:258px;width:114px"></div>
  <div class="abs spoke" style="left:700px;top:336px;width:114px"></div>

  <div class="abs hub">Verdell<br>Chiropractic</div>

  <div class="abs svc-label l" style="left:74px;top:171px">CHIROPRACTIC</div>
  <div class="abs svc-dot" style="left:330px;top:152px"><span></span></div>
  <div class="abs svc-label l" style="left:74px;top:249px">ACUPUNCTURE</div>
  <div class="abs svc-dot" style="left:330px;top:230px"><span></span></div>
  <div class="abs svc-label l" style="left:74px;top:317px">APPLIED<br>KINESIOLOGY</div>
  <div class="abs svc-dot" style="left:330px;top:308px"><span></span></div>

  <div class="abs svc-dot" style="left:814px;top:152px"><span></span></div>
  <div class="abs svc-label" style="left:888px;top:171px">MASSAGE</div>
  <div class="abs svc-dot" style="left:814px;top:230px"><span></span></div>
  <div class="abs svc-label" style="left:888px;top:249px">HOMEOPATHY</div>
  <div class="abs svc-dot" style="left:814px;top:308px"><span></span></div>
  <div class="abs svc-label" style="left:888px;top:307px">SPINAL<br>DECOMPRESSION<br>THERAPY</div>

  <div class="abs more-link">VIEW OTHER SERVICES</div>
</section>

<!-- faq -->
<section class="abs faq" role="img" aria-label="Photo of a chiropractor adjusting a patient's shoulders in a clinic"></section>
<div class="abs eyebrow" style="left:702px;top:1380px">Have any questions</div>
<h2 class="abs" style="left:702px;top:1393px;font-size:31px;font-weight:700;color:var(--blue-deep);letter-spacing:.5px">FAQS</h2>
<div class="abs faq-item open" style="top:1447px">The standard chunk of Lorem Ipsum?
  <svg viewBox="0 0 12 12"><path d="M3 7.5l3-3 3 3" fill="none" stroke="#fff" stroke-width="1.5"/></svg></div>
<p class="abs faq-answer" style="top:1500px">The point of using Lorem Ipsum is that it has a more-or-less normal distribution of letters, as opposed to using desktop publishing packages.</p>
<div class="abs faq-item" style="top:1599px">Where can I get some?
  <svg viewBox="0 0 12 12"><path d="M3 4.5l3 3 3-3" fill="none" stroke="#333" stroke-width="1.5"/></svg></div>
<div class="abs faq-item" style="top:1670px">Where does it come from?
  <svg viewBox="0 0 12 12"><path d="M3 4.5l3 3 3-3" fill="none" stroke="#333" stroke-width="1.5"/></svg></div>
<div class="abs faq-item" style="top:1741px">What is Lorem Ipsum?
  <svg viewBox="0 0 12 12"><path d="M3 4.5l3 3 3-3" fill="none" stroke="#333" stroke-width="1.5"/></svg></div>

<!-- testimonials -->
<section class="abs testimonials" role="img" aria-label="Faded photo of people stretching outdoors"></section>
<section class="abs" style="left:0;top:1872px;width:1200px;height:565px" aria-label="Testimonials">
  <div class="abs eyebrow" style="left:0;width:1200px;top:86px;text-align:center">Our happy clients</div>
  <h2 class="abs" style="left:0;width:1200px;top:99px;text-align:center;font-size:31px;font-weight:700;color:var(--blue-deep);letter-spacing:.5px">TESTIMONIALS</h2>

  <svg class="abs arrow" style="left:84px;top:315px" viewBox="0 0 16 16"><path d="M10 3L5 8l5 5" fill="none" stroke="#666" stroke-width="1.5"/></svg>
  <svg class="abs arrow" style="left:1102px;top:315px" viewBox="0 0 16 16"><path d="M6 3l5 5-5 5" fill="none" stroke="#666" stroke-width="1.5"/></svg>

  <div class="abs quote-card" style="left:113px">
    <p>I am an M.D., and advised many of my patients to consult with Dr. Marlow. Those who took my advice got better quickly. I, personally, have used Dr. Marlow's services on numerous occasions, have always found relief for my conditions, and have saved hundreds of dollars, which otherwise would have been spent on medications that might have had adverse side-effects.</p>
    <cite>RKT, M.D., Dalwood TX</cite>
  </div>
  <div class="abs qmark" style="left:209px;top:167px">“</div>
  <div class="abs qmark" style="left:439px;top:440px">”</div>

  <div class="abs quote-card" style="left:624px">
    <p>Prior to seeing Dr. Marlow, I had a headache for 18 straight days, as well as lower back and hip pain. The care I received was very professional, and I appreciated that I was given a choice of treatment. Now I have no headaches at all, and no back pain. Dr. Marlow and his staff were very courteous, nice, and caring. The care I received, although I was in severe pain...</p>
    <cite>MB, Dalwood, TX</cite>
  </div>
  <div class="abs qmark" style="left:720px;top:167px">“</div>
  <div class="abs qmark" style="left:950px;top:440px">”</div>
</section>

<!-- cta -->
<section class="abs cta">
  <p class="abs">Lorem Ipsum is simply dummy text of the printing.</p>
  <div class="abs btn">MAKE AN APPOINTMENT</div>
</section>

<!-- footer -->
<footer class="abs footer">
  <div class="abs brand">Verdell Chiropractic</div>
  <p class="abs blurb">There are many variations of passages of Lorem Ipsum available, but the majority have suffered alteration in some form, by injected humour, or randomised words.</p>
  <p class="abs copy">© Copyright 2018 &nbsp;|&nbsp; All Rights Reserved.</p>

  <h4 class="abs" style="left:437px">QUICK LINKS</h4>
  <ul class="abs" style="left:437px">
    <li>Home</li><li>Meet Dr. Marlow</li><li>Testimonials</li><li>FAQs Resources</li><li>Contact us</li>
  </ul>

  <h4 class="abs" style="left:656px">SERVICES</h4>
  <ul class="abs" style="left:656px">
    <li>Chiropractic</li><li>Acupuncture</li><li>Applied Kinesiology</li><li>Massage</li><li>Homeopathy</li><li>Spinal Decompression Therapy</li>
  </ul>

  <h4 class="abs" style="left:962px">CONTACT INFO</h4>
  <div class="abs info" style="left:962px">
    <div class="info-row"><svg viewBox="0 0 12 12"><path d="M6 1a3.5 3.5 0 0 1 3.5 3.5C9.5 7 6 11 6 11S2.5 7 2.5 4.5A3.5 3.5 0 0 1 6 1z" fill="#8dc63f"/><circle cx="6" cy="4.5" r="1.3" fill="#2b2b2b"/></svg><span>4870 Crestline Avenue West<br>Dalwood, TX 79301</span></div>
    <div class="info-row"><svg viewBox="0 0 12 12"><path d="M2.5 1.5l2.2 2.2-1.1 1.4a6 6 0 0 0 3.3 3.3l1.4-1.1 2.2 2.2-1.4 1.4C4.5 10.9 1.1 7.5 1.1 2.9z" fill="#8dc63f"/></svg><span>555.210.4400</span></div>
    <div class="info-row"><svg viewBox="0 0 12 12"><rect x="1" y="2" width="10" height="8" rx="1" fill="#8dc63f"/><rect x="3" y="3.5" width="6" height="2" fill="#2b2b2b"/></svg><span>555.210.4410</span></div>
    <div class="info-row"><svg viewBox="0 0 12 12"><rect x="1" y="2.5" width="10" height="7" rx="1" fill="#8dc63f"/><path d="M1.5 3l4.5 3.5L10.5 3" fill="none" stroke="#2b2b2b" stroke-width="1"/></svg><span>info@mirvaton.com</span></div>
  </div>
</footer>

</body>
</html>
```